The Wellness Barn Business Card

Info for the front..... (in whichever order and layout looks best)
Carla Penhallow
Physiotherapist
4/37 Upper Creekbank Rd
Tallowbrook
QLD 4712
0462305178
carlapenhallow57@mailbox.example
www.thewellnessbarn.example.au
on the back I would like to be able to write appointments so probably just that heading with lines.
I like a sort of rustic style but mostly professional, colours in naturals, beige, brown, green etc. I dont mind if the logo colour is changed slightly to suit.

```html
<!DOCTYPE html>
<html lang="en">
<head>
<meta charset="utf-8">
<title>The Wellness Barn – Business Card</title>
<link href="https://fonts.googleapis.com/css2?family=Arimo:wght@400;700&display=swap" rel="stylesheet">
<style>
  :root{
    --green:#2d4a1e;
    --green-soft:#4c6340;
    --card:#ffffff;
    --stage:#2a2a2a;
    --rule:#8a9a80;
  }
  *{margin:0;padding:0;box-sizing:border-box}
  html,body{width:1200px;height:874px;overflow:hidden;background:var(--stage)}
  body{position:relative;font-family:"Arimo",Arial,sans-serif;color:var(--green)}
  .card{position:absolute;width:600px;height:343px;background:var(--card);border-radius:18px;border-bottom:3px solid var(--green)}
  .card-back{left:500px;top:60px}
  .card-front{left:100px;top:460px}

  /* back */
  .appt-title{position:absolute;left:34px;top:28px;font-size:23px;font-weight:700}
  .back-brand{position:absolute;right:28px;top:30px;width:92px;font-size:17px;font-weight:700;line-height:1.05;text-align:center}
  .field{position:absolute;left:34px;display:flex;align-items:flex-end;font-size:15px;color:var(--green-soft)}
  .field .line{flex:1;border-bottom:1.5px dotted var(--rule);margin-left:8px;height:14px}
  .f-name{top:74px;width:420px}
  .f-date{top:108px;width:420px}
  .f-time{top:178px;width:532px}
  .f-time .suffix{margin-left:8px}
  .f-note{top:212px;width:532px}
  .f-extra{position:absolute;left:34px;top:242px;width:532px;border-bottom:1.5px dotted var(--rule)}
  .days{position:absolute;left:34px;top:144px;width:532px;display:flex;justify-content:space-between;font-size:15px;color:var(--green-soft)}
  .day{display:flex;align-items:center;gap:6px}
  .box{width:15px;height:15px;border:1.5px solid var(--green-soft)}
  .notice{position:absolute;left:40px;right:40px;top:270px;text-align:center;font-size:13px;line-height:1.35;color:#555}

  /* front */
  .brand{position:absolute;left:34px;top:100px;width:230px;display:flex;align-items:center;gap:12px}
  .brand-dot{width:22px;height:22px;border-radius:50%;background:var(--green);flex:none}
  .brand-name{font-size:36px;font-weight:700;line-height:1.05;color:var(--green)}
  .divider{position:absolute;left:300px;top:40px;bottom:40px;width:1px;background:linear-gradient(transparent,#bbb 20%,#bbb 80%,transparent)}
  .info{position:absolute;left:326px;top:46px;color:#333}
  .person{font-size:24px;font-weight:700;color:var(--green)}
  .role{font-size:14px;color:#777;margin-bottom:12px}
  .address{font-size:15px;line-height:1.3;margin-bottom:12px}
  .contact{list-style:none;font-size:15px;line-height:1.45}
  .contact li{display:flex;align-items:center;gap:9px}
  .contact svg{width:13px;height:13px;fill:var(--green);flex:none}
</style>
</head>
<body>

<section class="card card-back" aria-label="Appointment side">
  <h2 class="appt-title">Next Appointment</h2>
  <div class="back-brand">The Wellness Barn</div>
  <div class="field f-name">Name :<span class="line"></span></div>
  <div class="field f-date">Date :<span class="line"></span></div>
  <div class="days">
    <span class="day">Sun <span class="box"></span></span>
    <span class="day">Mon <span class="box"></span></span>
    <span class="day">Tue <span class="box"></span></span>
    <span class="day">Wed <span class="box"></span></span>
    <span class="day">Thu <span class="box"></span></span>
    <span class="day">Fri <span class="box"></span></span>
    <span class="day">Sat <span class="box"></span></span>
  </div>
  <div class="field f-time">Time :<span class="line"></span><span class="suffix">AM/PM</span></div>
  <div class="field f-note">Note :<span class="line"></span></div>
  <div class="f-extra"></div>
  <p class="notice">Please give me 24 hours notice if you are unable to keep your appointment or a cancellation fee may be charged.</p>
</section>

<section class="card card-front" aria-label="Contact side">
  <div class="brand">
    <span class="brand-dot"></span>
    <span class="brand-name">The Wellness Barn</span>
  </div>
  <div class="divider"></div>
  <div class="info">
    <div class="person">Carla Penhallow</div>
    <div class="role">Physiotherapist</div>
    <address class="address" style="font-style:normal">
      4/37 Upper Creekbank Rd<br>Tallowbrook<br>QLD 4712
    </address>
    <ul class="contact">
      <li><svg viewBox="0 0 24 24"><path d="M6.6 10.8a15.1 15.1 0 0 0 6.6 6.6l2.2-2.2a1 1 0 0 1 1-.25 11.4 11.4 0 0 0 3.6.57 1 1 0 0 1 1 1V20a1 1 0 0 1-1 1A17 17 0 0 1 3 4a1 1 0 0 1 1-1h3.5a1 1 0 0 1 1 1c0 1.25.2 2.45.57 3.57a1 1 0 0 1-.25 1z"/></svg>0462305178</li>
      <li><svg viewBox="0 0 24 24"><path d="M2 5h20v14H2z M2 5l10 8 10-8" /></svg>carlapenhallow57@mailbox.example</li>
      <li><svg viewBox="0 0 24 24"><circle cx="12" cy="12" r="10"/></svg>www.thewellnessbarn.example.au</li>
    </ul>
  </div>
</section>

</body>
</html>
```